Fun footwear company needs a media card!

We are a fun footwear company called 'Puddle Hops' we are looking for a small media card to be sent out with our products.
The media card will showcase or newest product 'Puddle Parkas' - it needs to include a small caption reading
'Hello, adventurer. It’s time to stomp around in the rain.Tag your travels @goskipwade #phops or visit us at splashpage.com/goskipwade'
We would like to include or logo (attached)
Also have something similar to the previous media card (attached)
I have attached an image of the product (please feel free to not include this is you think it does not work)
As we are a fun brand, all of our promotional media needs to be bright and fit in with our brand.
Visit our website to see our products www.pudhops.com.au

```html
<!DOCTYPE html>
<html lang="en">
<head>
<meta charset="utf-8">
<title>Puddle Hops Media Card</title>
<link href="https://fonts.googleapis.com/css2?family=Space+Mono:wght@400;700&display=swap" rel="stylesheet">
<style>
  :root {
    --page: #ffffff;
    --card: #ffffff;
    --card-edge: #c9c9c9;
    --brand-red: #c62a37;
    --brand-red-soft: #eec3c7;
    --brand-blue: #2a8ec6;
    --sky-blue: #21a4e0;
    --ink: #222222;
    --rain-light: #eef7fc;
    --rain-mid: #cfe6f4;
  }
  * { margin: 0; padding: 0; box-sizing: border-box; }
  html, body {
    width: 1200px; height: 1138px; overflow: hidden;
    background: var(--page);
    font-family: "Space Mono", monospace;
  }
  .canvas { position: relative; width: 1200px; height: 1138px; }

  .card {
    position: absolute; left: 86px; width: 1027px;
    background: var(--card);
    border: 1px solid var(--card-edge);
    overflow: hidden;
  }
  .card--front { top: 28px; height: 520px; }
  .card--back { top: 587px; height: 521px; }

  .brand-name {
    position: absolute; left: 0; right: 0; top: 196px;
    text-align: center;
    font-weight: 700; font-size: 76px; line-height: 90px;
    color: var(--sky-blue);
    white-space: nowrap;
  }

  .message {
    position: absolute; left: 0; top: 0; width: 590px; height: 521px;
    font-family: "Space Mono", monospace; font-weight: 700;
  }
  .message .band { fill: var(--brand-red); }
  .message .accent { fill: var(--brand-red-soft); }
  .message .rule-dotted { stroke: var(--brand-red); stroke-width: 3; stroke-dasharray: 2 3; }
  .message .rule-dashed { stroke: var(--brand-red); stroke-width: 3; stroke-dasharray: 7 4; }
  .message .rule-solid { fill: var(--brand-red); }
  .message .band-text { fill: #ffffff; font-size: 38px; }
  .message .phrase { fill: var(--ink); font-size: 29px; }
  .message .shout { fill: var(--brand-blue); font-size: 62px; }
  .message .social-tags { fill: var(--brand-blue); font-size: 34px; }
  .message .visit { fill: var(--ink); font-size: 18px; }
  .message .web-box { fill: var(--brand-blue); }
  .message .web-text { fill: #ffffff; font-size: 18px; }

  .product-photo {
    position: absolute; left: 600px; top: 0; width: 427px; height: 521px;
    background: linear-gradient(160deg, var(--rain-light) 0%, var(--rain-mid) 100%);
  }
</style>
</head>
<body>
<main class="canvas">

  <section class="card card--front" aria-label="Card front">
    <h1 class="brand-name">Puddle Hops</h1>
  </section>

  <section class="card card--back" aria-label="Card back">
    <svg class="message" viewBox="0 0 590 521" aria-label="Hello, adventurer. It’s time to stomp around in the rain. Tag your travels @goskipwade #phops or visit us at splashpage.com/goskipwade">
      <rect class="band" x="0" y="85" width="580" height="67"/>
      <text class="band-text" x="50" y="133" textLength="518" lengthAdjust="spacingAndGlyphs">HELLO, ADVENTURER</text>

      <line class="rule-dotted" x1="0" y1="175" x2="341" y2="175"/>
      <text class="phrase" x="50" y="208" textLength="286" lengthAdjust="spacingAndGlyphs">IT’S TIME TO</text>
      <line class="rule-dotted" x1="0" y1="217" x2="341" y2="217"/>
      <text class="shout" x="346" y="219" textLength="222" lengthAdjust="spacingAndGlyphs">STOMP</text>

      <line class="rule-dashed" x1="0" y1="232" x2="388" y2="232"/>
      <rect class="accent" x="0" y="238" width="47" height="28" role="img" aria-label="Red hatched stripe accent"/>
      <text class="phrase" x="50" y="265" textLength="330" lengthAdjust="spacingAndGlyphs">AROUND IN THE</text>
      <line class="rule-dashed" x1="0" y1="274" x2="388" y2="274"/>
      <text class="shout" x="395" y="275" textLength="173" lengthAdjust="spacingAndGlyphs">RAIN</text>

      <rect class="band" x="0" y="293" width="580" height="61"/>
      <text class="band-text" x="50" y="338" textLength="520" lengthAdjust="spacingAndGlyphs">TAG YOUR TRAVELS</text>

      <text class="social-tags" x="50" y="389" textLength="518" lengthAdjust="spacingAndGlyphs">@goskipwade #phops</text>
      <rect class="rule-solid" x="0" y="405" width="580" height="3"/>

      <text class="visit" x="53" y="431" textLength="187" lengthAdjust="spacingAndGlyphs">or visit us at</text>
      <rect class="web-box" x="250" y="413" width="327" height="26"/>
      <text class="web-text" x="263" y="431" textLength="301" lengthAdjust="spacingAndGlyphs">splashpage.com/goskipwade</text>
    </svg>

    <div class="product-photo" role="img" aria-label="Photo of a smiling model wearing a clear blue-trimmed Puddle Parka with the hood up, surrounded by falling blue raindrops"></div>
  </section>

</main>
</body>
</html>
```